Rising Paths Web Design

I am starting a new company that will provide LIFE COACHING services - I have tried to design a website, but it's too complicated. Right now, it's just me - I'm the only person that will provide services through the website - I have used artmarket to purchase a logo (see below). I want to be able to update the website myself, but need a template - basic design. Because I am not technologically savvy enough to explain in words - I basically want to have a website that will provide basic information about my services (coaching), a page about me and my background, hopefully scheduling possibilities, and testimonials — also a page for writing/blogs. I bought a website through NetHarbor - so when I have a template, I guess I”d use that - but maybe I’ll need to work with a designer to actually get it up on the internet. I have a head shot that I’ll upload, too.
Target Market(s)
Clients from the independent (private school) world - teachers, administrators
Number of Pages Required
4 page
Look and feel
Each slider illustrates characteristics of the customer's brand and the style your logo design should communicate.

```html
<!DOCTYPE html>
<html lang="en">
<head>
<meta charset="utf-8">
<title>Rising Paths – Coaching Website</title>
<link rel="stylesheet" href="https://fonts.googleapis.com/css2?family=Inter:wght@400;600;700&family=Montserrat:wght@500&display=swap">
<style>
:root{
  --board:#c5c5c7;
  --teal:#17a398;
  --teal-dark:#0f877c;
  --teal-text:#1a9c95;
  --label:#1d8c95;
  --ink:#2b2b2b;
  --muted:#555;
  --panel:#efeeef;
  --card:#e3e3e3;
  --soft:#f0f0f0;
  --white:#fff;
}
*{margin:0;padding:0;box-sizing:border-box}
html,body{width:742px;height:1200px;overflow:hidden;background:var(--board);font-family:"Inter",Arial,sans-serif;color:var(--ink)}
.board{position:relative;width:742px;height:1200px;overflow:hidden}
.frame{position:absolute;overflow:hidden;background:var(--white)}
.frame--full{left:67px;top:37px;width:254px;height:1139px}
.frame--zoom{left:346px;top:569px;width:380px;height:631px}
.page{position:absolute;left:0;top:0;width:370px;height:1658px;transform-origin:0 0;background:var(--white)}
.frame--full .page{transform:scale(.6865)}
.frame--zoom .page{transform:scale(1.027)}
.page *{position:absolute}
.page .flow,.page .flow *{position:static}
.band{left:0;width:370px}
.hero{top:0;height:171px}
.hero svg{left:0;top:0}
.brand-box{left:150px;top:0;width:70px;height:50px;background:var(--white);border-radius:0 0 4px 4px;display:flex;align-items:center;justify-content:center;gap:3px}
.brand-box .dot{position:static;width:5px;height:5px;border-radius:50%;background:var(--teal)}
.brand-box .name{position:static;font-size:6px;color:var(--teal-text);font-weight:600;white-space:nowrap}
.hero-title{left:0;top:56px;width:370px;text-align:center;color:var(--white);font-size:10.5px;line-height:13px}
.btn{height:10px;background:var(--teal);color:var(--white);font-size:3.6px;font-weight:700;letter-spacing:.2px;display:flex;align-items:center;justify-content:center;text-transform:uppercase}
.btn--light{background:var(--white);color:var(--teal)}
.h-teal{color:var(--teal-text);font-weight:700;font-size:6.4px;text-transform:uppercase}
.h-white{color:var(--white);font-weight:700;font-size:6.4px;text-transform:uppercase;text-align:center;width:370px;left:0}
.about-text{left:48px;top:222px;width:136px;font-size:4.5px;line-height:6.9px;color:var(--ink)}
.portrait{left:215px;top:214px;width:112px;height:112px;border-radius:50%;background:radial-gradient(circle at 50% 45%,#d8c7b2 0 30%,#b9a68d 45%,#6f6a62 75%,#3e3d3a)}
.badge{top:309px;width:28px;height:28px}
.badge--square{left:48px;background:#1f5f8a;border-radius:2px}
.badge--round{left:84px;border-radius:50%;border:3px solid #2c90c9;background:var(--white)}
.why{top:377px;height:179px;background:var(--teal)}
.col{width:76px;color:var(--white)}
.col svg{position:absolute;left:0;top:0}
.col-title{top:25px;left:0;width:76px;font-size:4.6px;font-weight:700;line-height:5.4px;text-transform:uppercase}
.col-text{top:38px;left:0;width:70px;font-size:3.9px;line-height:5.9px}
.strip{top:556px;height:67px;background:var(--teal-dark)}
.strip-text{left:30px;top:15px;width:310px;text-align:center;font-size:4.3px;line-height:6px;color:var(--white);font-weight:700}
.quotes{top:623px;height:213px}
.quote-card{left:99px;top:48px;width:171px;height:107px;background:var(--card)}
.avatar{left:10px;top:18px;width:17px;height:17px;border-radius:50%;background:linear-gradient(#c9a78a,#8a6e58)}
.quote-text{left:10px;top:42px;width:150px;font-size:3.6px;line-height:5px}
.quote-name{left:10px;top:88px;font-size:3.3px}
.dots{left:174px;top:169px;display:flex;gap:4px}
.dots i{position:static;display:block;width:3px;height:3px;border-radius:50%;background:#cfcfcf}
.dots i:first-child{background:var(--teal)}
.photos{top:836px;height:92px}
.photo{top:0;height:92px}
.method{top:928px;height:158px;background:var(--teal)}
.mcol{top:57px;width:100px;color:var(--white)}
.mcol-title{left:0;top:0;width:100px;font-size:4.4px;font-weight:700;line-height:5.4px;text-transform:uppercase}
.mcol-text{left:0;top:18px;width:95px;font-size:3.5px;line-height:5.1px}
.areyou{top:1086px;height:143px}
.areyou-photo{left:0;top:0;width:164px;height:143px;background:linear-gradient(135deg,#e8e8e8,#9a9a9a 55%,#4b4b4b)}
.areyou-list{left:176px;top:44px;width:184px;font-size:3.3px;line-height:4.5px}
.areyou-list p{position:static;margin-bottom:3.4px;padding-left:4px;text-indent:-4px}
.transform{top:1229px;height:61px;background:var(--teal-dark)}
.blog{top:1290px;height:206px;background:var(--soft)}
.post{top:49px;width:102px}
.post-img{left:0;top:0;width:102px;height:69px}
.post-date{left:0;top:74px;font-size:2.8px;color:#777}
.post-title{left:0;top:79px;width:100px;font-size:4.1px;line-height:5px;font-weight:700}
.post-more{left:0;top:98px;font-size:3.6px;color:var(--teal-text);text-decoration:underline}
.faq{top:1496px;height:140px}
.faq-item{left:60px;width:253px;border:.6px solid var(--teal);display:flex;align-items:center;justify-content:space-between;padding:0 6px;font-size:3.6px;color:var(--teal-text);line-height:4.6px}
.faq-item span,.faq-item b{position:static}
.faq-item b{font-weight:400;font-size:6px}
.footer{top:1636px;height:22px;background:#e6e6e6;font-size:2.8px;text-align:center;line-height:22px;color:#444}
/* form panel */
.form-panel{position:absolute;left:353px;top:96px;width:366px;height:316px;background:var(--panel)}
.form-panel *{position:absolute}
.form-title{left:0;top:31px;width:366px;text-align:center;font-size:8.8px;font-weight:600;color:var(--teal-text)}
.form-intro{left:50px;top:60px;width:266px;text-align:center;font-size:5.3px;line-height:9.5px}
.field{font-size:5.4px;font-weight:600}
.line{height:.8px;background:#9a9a9a}
.submit{left:148px;top:205px;width:75px;height:14px;background:var(--teal);color:var(--white);font-size:4.3px;font-weight:700;display:flex;align-items:center;justify-content:center}
.legal{left:44px;top:241px;width:278px;text-align:center;font-size:5.2px;line-height:9.4px}
.caption{position:absolute;left:396px;top:434px;font-family:"Montserrat",Arial,sans-serif;font-weight:500;font-size:16.6px;color:var(--label);white-space:nowrap;letter-spacing:.2px}
</style>
</head>
<body>
<main class="board">

<!-- Full home page -->
<section class="frame frame--full">
<div class="page">
  <header class="band hero">
    <svg width="370" height="171" viewBox="0 0 370 171" role="img" aria-label="Black and white photo of a person in a field with arms raised">
      <defs><linearGradient id="heroA" x1="0" y1="0" x2="1" y2="1"><stop offset="0" stop-color="#3b3b3b"/><stop offset=".55" stop-color="#6e6e6e"/><stop offset="1" stop-color="#3c3c3c"/></linearGradient></defs>
      <rect width="370" height="171" fill="url(#heroA)"/>
      <path d="M0 134 C60 118 130 130 210 158 L0 171Z" fill="#17a398"/>
      <path d="M0 158 C70 130 140 160 220 164 C290 168 340 130 370 108 L370 171 L0 171Z" fill="#fff"/>
    </svg>
    <div class="brand-box"><span class="dot"></span><span class="name">Rising Paths</span></div>
    <h1 class="hero-title" style="font-weight:400">Do you need to make some concrete changes?<br>Let me help &amp; show you how</h1>
    <div class="btn" style="left:150px;top:89px;width:72px">Schedule Consultation</div>
  </header>

  <h2 class="h-teal" style="left:48px;top:205px">About Me</h2>
  <p class="about-text">Lorem ipsum dolor sit amet, consectetur adipiscing elit. Ac euismod tellus morbi cursus. Pulvinar vel interdum commodo suspendisse at tortor lacus, tortor adipiscing. Mi volutpat, purus dolor ut in nulla tellus malesuada. Sit tristique placerat feugiat tellus magna. Quis morbi sed erat sed consectetur sed elit sit aliquam. Enim sem arcu nisl arcu massa. Magna ipsum proin sollicitudin ipsum viverra vulputate porttitor. In scelerisque et a quisque sollicitudin est eu. A lectus justo, diam enim id nec vitae erat. Euismod sit bibendum scelerisque convallis sit nunc euismod leo. Ullamcorper ac neque hendrerit quis orci risus pellentesque. Cursus dolor, cursus consequat quisque ac.</p>
  <div class="portrait" role="img" aria-label="Head shot of the coach"></div>
  <div class="badge badge--square" role="img" aria-label="Coaching certification badge"></div>
  <div class="badge badge--round" role="img" aria-label="Coaching federation member badge"></div>

  <section class="band why">
    <h2 class="h-white" style="top:29px">Why Life Coaching?</h2>
    <div class="col" style="left:27px;top:57px">
      <svg width="18" height="18" viewBox="0 0 18 18" fill="none" stroke="#fff" stroke-width="1.2"><circle cx="9" cy="9" r="7.5"/><path d="M5.5 10.5c1 2 6 2 7 0M6 7h1.5M10.5 7H12"/></svg>
      <h3 class="col-title">Being Happy</h3>
      <p class="col-text">With yourself and the people around you. Discover what sparks your joy and what's important in your life so you can create constant happiness, fulfilment and success in your personal and professional life.</p>
    </div>
    <div class="col" style="left:112px;top:57px">
      <svg width="18" height="18" viewBox="0 0 18 18" fill="none" stroke="#fff" stroke-width="1.2"><path d="M4 14 L14 4 M9 4 H14 V9"/><path d="M3 10 l2 3 3 2"/></svg>
      <h3 class="col-title">Gain Clarity<br>in Your Life</h3>
      <p class="col-text">Get crystal clear on your life purpose and mission now so you can stop feeling lost and stuck next year. That means, you'll move with certainty and create the life you would absolutely love and adore.</p>
    </div>
    <div class="col" style="left:197px;top:57px">
      <svg width="18" height="18" viewBox="0 0 18 18" fill="none" stroke="#fff" stroke-width="1.2"><circle cx="9" cy="9" r="7.5"/><circle cx="9" cy="9" r="4.5"/><circle cx="9" cy="9" r="1.5"/></svg>
      <h3 class="col-title">Fulfilling Potential</h3>
      <p class="col-text">Overcome roadblocks and achieve your goals faster and easier. Get over fears, have the courage to leave the job you hate or pursue your destiny so you can feel more fulfilled and alive every single day.</p>
    </div>
    <div class="col" style="left:284px;top:57px">
      <svg width="18" height="18" viewBox="0 0 18 18" fill="none" stroke="#fff" stroke-width="1.2"><path d="M5 17V2M5 2h9l-2 3 2 3H5"/><circle cx="2.5" cy="11" r="1.2"/></svg>
      <h3 class="col-title">Be an Effective<br>Leader</h3>
      <p class="col-text">At work, you command genuine respect and gratitude, allowing your subordinates to give you their best performance. At home, your children adore you for being the most nurturing parent, bringing out the best in them.</p>
    </div>
  </section>

  <section class="band strip">
    <p class="strip-text">Its imperative to connect well with your chosen life coach, and to make sure that you are a good match.<br>Life coaching is a journey through thoughts, feelings and commitment to change.</p>
    <div class="btn btn--light" style="left:150px;top:41px;width:70px">Schedule Consultation</div>
  </section>

  <section class="band quotes">
    <h2 class="h-teal" style="left:0;top:17px;width:370px;text-align:center;font-size:5.8px">What Results Coaching Clients Are Saying</h2>
    <div class="quote-card">
      <div class="avatar" role="img" aria-label="Client profile photo"></div>
      <p class="quote-text">Lorem ipsum dolor sit amet, consectetur adipiscing elit. Hac justo vitae eget imperdiet mi mi massa. Lectus sit magna nunc lorem ut id vestibulum amet. Feugiat cras lorem ipsum lectus. Phasellus vitae ac ullamcorper in pulvinar neque, neque, tincidunt magna.</p>
      <p class="quote-name"><b>John Doe,</b> Business Owner</p>
    </div>
    <div class="dots"><i></i><i></i><i></i></div>
  </section>

  <div class="band photos">
    <div class="photo" style="left:0;width:122px;background:linear-gradient(135deg,#d9d4cf,#7a6e66 60%,#3a3633)" role="img" aria-label="Woman smiling at a desk in an office"></div>
    <div class="photo" style="left:123px;width:122px;background:linear-gradient(135deg,#e6e6e6,#8b8b8b 50%,#4d4d4d)" role="img" aria-label="Happy couple laughing outdoors"></div>
    <div class="photo" style="left:246px;width:124px;background:linear-gradient(135deg,#f0efec,#b9b2a8 55%,#5a5148)" role="img" aria-label="Woman working on a laptop at home"></div>
  </div>

  <section class="band method">
    <h2 class="h-white" style="top:28px">Why My Method Deliver Results</h2>
    <div class="mcol" style="left:30px">
      <h3 class="mcol-title">No-Nonsense Approach</h3>
      <p class="mcol-text">Write talk therapy and motivation talks can make us feel better, you may already know that they rarely ever solve the problem. Instead, real results only come when you truly accept and take action to live the hard truth. This is difficult to do on your own. But with the help of my approach and deep-dive coaching, it doesn't have to be that way any longer.</p>
    </div>
    <div class="mcol" style="left:144px">
      <h3 class="mcol-title">Lasting Results by<br>Resolving Inner Conflicts</h3>
      <p class="mcol-text">Yes, seminars, motivational talks and coaching can give you results. But you may find the results to be temporary, often lasting up to only 6 months. This is because relying on willpower and good feelings can only take us so far. To lock in the transformation and results, we have to go deeper into your mind and resolve the limiting belief that's still holding you back.</p>
    </div>
    <div class="mcol" style="left:262px">
      <h3 class="mcol-title">Over ... Years of<br>Professional Coaching<br>Experience</h3>
      <p class="mcol-text" style="top:24px">It's no secret that experience does matter. Having an experienced, proven coach who knows the potholes to avoid can save you up to years of unnecessary suffering. In fact, it pains me to see clients coming to me only when the damage has been done and decades have been wasted. With my years of experience and proven strategies, rest assure that you are in safe hands.</p>
    </div>
  </section>

  <section class="band areyou">
    <div class="areyou-photo" role="img" aria-label="Stressed man holding his head at a desk"></div>
    <h2 class="h-teal" style="left:176px;top:30px">Are You...</h2>
    <div class="areyou-list">
      <p>• stuck mulling over the future, constantly worrying about the worst possible outcome and unclear what the next course of action should be?</p>
      <p>• having a sense that problems never improve, despite receiving help from friends and family</p>
      <p>• having difficulty concentrating on work, unmotivated and feel like you're getting burnt out</p>
      <p>• unhappy in your relationship(s)... but don't know what's wrong even after trying out many options to address the problem?</p>
      <p>• read a lot of books about personal development/self-help but can't seem to correct your behavior?</p>
    </div>
  </section>

  <section class="band transform">
    <h2 class="h-white" style="top:14px;font-size:6.6px;font-weight:600">Transform Your Mindset and Crush Your Goals</h2>
    <div class="btn btn--light" style="left:150px;top:35px;width:70px">Schedule Consultation</div>
  </section>

  <section class="band blog">
    <h2 class="h-teal" style="left:0;top:26px;width:370px;text-align:center">Blog</h2>
    <article class="post" style="left:21px">
      <div class="post-img" style="background:linear-gradient(#5aa6e0,#bfe0f5 55%,#d9d2c4)" role="img" aria-label="Wooden pier stretching into the sea"></div>
      <p class="post-date">24 July 2022</p>
      <h3 class="post-title">You don't know how good you are until you do it</h3>
      <p class="post-more">Read More</p>
    </article>
    <article class="post" style="left:135px">
      <div class="post-img" style="background:radial-gradient(circle at 70% 40%,#c02a35 0 18%,#eee 40%,#d8d8d8)" role="img" aria-label="Red mug in the snow"></div>
      <p class="post-date">24 July 2022</p>
      <h3 class="post-title">You can be a better version of yourself when you decide</h3>
      <p class="post-more">Read More</p>
    </article>
    <article class="post" style="left:248px">
      <div class="post-img" style="background:linear-gradient(135deg,#3a3a3a,#b9b3ad 50%,#efe9e2)" role="img" aria-label="Hands writing in a notebook at a desk"></div>
      <p class="post-date">24 July 2022</p>
      <h3 class="post-title" style="font-weight:400">Worry doesn't push you forward, action does!</h3>
      <p class="post-more">Read More</p>
    </article>
    <div class="btn" style="left:144px;top:172px;width:70px;height:13px">Read More</div>
  </section>

  <section class="band faq">
    <h2 class="h-teal" style="left:0;top:27px;width:370px;text-align:center">FAQ</h2>
    <div class="faq-item" style="top:47px;height:17px"><span>Should I not get a life coach?</span><b>›</b></div>
    <div class="faq-item" style="top:68px;height:21px"><span>how are you different from other methods out there such<br>as counseling and transformation workshops?</span><b>›</b></div>
    <div class="faq-item" style="top:91px;height:17px"><span>do you offer online sessions?</span><b>›</b></div>
  </section>

  <footer class="band footer">Copyright ©Rising Paths, all rights reserved</footer>
</div>
</section>

<!-- Scheduling form -->
<section class="form-panel">
  <h2 class="form-title">Are You Ready to Maximise Your Life?</h2>
  <p class="form-intro">Simple fill in the form for a free phone consultation to decide if we are a good fit. You can ask as many questions as you want to clarify your doubts.</p>
  <span class="field" style="left:44px;top:108px">First Name</span>
  <span class="field" style="left:186px;top:108px">Last Name</span>
  <div class="line" style="left:44px;top:124px;width:131px"></div>
  <div class="line" style="left:186px;top:124px;width:131px"></div>
  <span class="field" style="left:44px;top:136px">Phone Number</span>
  <span class="field" style="left:186px;top:136px">Email</span>
  <div class="line" style="left:44px;top:151px;width:131px"></div>
  <div class="line" style="left:186px;top:151px;width:131px"></div>
  <span class="field" style="left:44px;top:168px">Occupation</span>
  <div class="line" style="left:44px;top:184px;width:273px"></div>
  <div class="submit">SUBMIT</div>
  <p class="legal">By entering your information on the Rising Paths website, you agree that we may collect and use your personal information for marketing, and for other purposes, as set forth in our Privacy Policy, which we encourage you to review.</p>
</section>

<p class="caption">Form Schedulling direct to email</p>

<!-- Close-up of the top of the home page -->
<section class="frame frame--zoom">
<div class="page">
  <header class="band hero">
    <svg width="370" height="171" viewBox="0 0 370 171" role="img" aria-label="Black and white photo of a person in a field with arms raised">
      <defs><linearGradient id="heroB" x1="0" y1="0" x2="1" y2="1"><stop offset="0" stop-color="#3b3b3b"/><stop offset=".55" stop-color="#6e6e6e"/><stop offset="1" stop-color="#3c3c3c"/></linearGradient></defs>
      <rect width="370" height="171" fill="url(#heroB)"/>
      <path d="M0 134 C60 118 130 130 210 158 L0 171Z" fill="#17a398"/>
      <path d="M0 158 C70 130 140 160 220 164 C290 168 340 130 370 108 L370 171 L0 171Z" fill="#fff"/>
    </svg>
    <div class="brand-box"><span class="dot"></span><span class="name">Rising Paths</span></div>
    <h1 class="hero-title" style="font-weight:400">Do you need to make some concrete changes?<br>Let me help &amp; show you how</h1>
    <div class="btn" style="left:150px;top:89px;width:72px">Schedule Consultation</div>
  </header>

  <h2 class="h-teal" style="left:48px;top:205px">About Me</h2>
  <p class="about-text">Lorem ipsum dolor sit amet, consectetur adipiscing elit. Ac euismod tellus morbi cursus. Pulvinar vel interdum commodo suspendisse at tortor lacus, tortor adipiscing. Mi volutpat, purus dolor ut in nulla tellus malesuada. Sit tristique placerat feugiat tellus magna. Quis morbi sed erat sed consectetur sed elit sit aliquam. Enim sem arcu nisl arcu massa. Magna ipsum proin sollicitudin ipsum viverra vulputate porttitor. In scelerisque et a quisque sollicitudin est eu. A lectus justo, diam enim id nec vitae erat. Euismod sit bibendum scelerisque convallis sit nunc euismod leo. Ullamcorper ac neque hendrerit quis orci risus pellentesque. Cursus dolor, cursus consequat quisque ac.</p>
  <div class="portrait" role="img" aria-label="Head shot of the coach"></div>
  <div class="badge badge--square" role="img" aria-label="Coaching certification badge"></div>
  <div class="badge badge--round" role="img" aria-label="Coaching federation member badge"></div>

  <section class="band why">
    <h2 class="h-white" style="top:29px">Why Life Coaching?</h2>
    <div class="col" style="left:27px;top:57px">
      <svg width="18" height="18" viewBox="0 0 18 18" fill="none" stroke="#fff" stroke-width="1.2"><circle cx="9" cy="9" r="7.5"/><path d="M5.5 10.5c1 2 6 2 7 0M6 7h1.5M10.5 7H12"/></svg>
      <h3 class="col-title">Being Happy</h3>
      <p class="col-text">With yourself and the people around you. Discover what sparks your joy and what's important in your life so you can create constant happiness, fulfilment and success in your personal and professional life.</p>
    </div>
    <div class="col" style="left:112px;top:57px">
      <svg width="18" height="18" viewBox="0 0 18 18" fill="none" stroke="#fff" stroke-width="1.2"><path d="M4 14 L14 4 M9 4 H14 V9"/><path d="M3 10 l2 3 3 2"/></svg>
      <h3 class="col-title">Gain Clarity<br>in Your Life</h3>
      <p class="col-text">Get crystal clear on your life purpose and mission now so you can stop feeling lost and stuck next year. That means, you'll move with certainty and create the life you would absolutely love and adore.</p>
    </div>
    <div class="col" style="left:197px;top:57px">
      <svg width="18" height="18" viewBox="0 0 18 18" fill="none" stroke="#fff" stroke-width="1.2"><circle cx="9" cy="9" r="7.5"/><circle cx="9" cy="9" r="4.5"/><circle cx="9" cy="9" r="1.5"/></svg>
      <h3 class="col-title">Fulfilling Potential</h3>
      <p class="col-text">Overcome roadblocks and achieve your goals faster and easier. Get over fears, have the courage to leave the job you hate or pursue your destiny so you can feel more fulfilled and alive every single day.</p>
    </div>
    <div class="col" style="left:284px;top:57px">
      <svg width="18" height="18" viewBox="0 0 18 18" fill="none" stroke="#fff" stroke-width="1.2"><path d="M5 17V2M5 2h9l-2 3 2 3H5"/><circle cx="2.5" cy="11" r="1.2"/></svg>
      <h3 class="col-title">Be an Effective<br>Leader</h3>
      <p class="col-text">At work, you command genuine respect and gratitude, allowing your subordinates to give you their best performance. At home, your children adore you for being the most nurturing parent, bringing out the best in them.</p>
    </div>
  </section>

  <section class="band strip">
    <p class="strip-text">Its imperative to connect well with your chosen life coach, and to make sure that you are a good match.<br>Life coaching is a journey through thoughts, feelings and commitment to change.</p>
    <div class="btn btn--light" style="left:150px;top:41px;width:70px">Schedule Consultation</div>
  </section>
</div>
</section>

</main>
</body>
</html>
```